Modern Business Card for Industrial Company

We need business cards updated with modern fonts and make it look more technical, sharp and clean. The logo should not be changed, but we are looking for fresh solutions for how other information on the card is laid out in an interesting way. The company provides machinery and services to the ceramic industry and deals with cutting-edge technology. The design should reflect a technologically advanced and modern company that deals with the latest European technologies.

Font styles to use
Sans Serif

Requirements
Must have
• Modern fonts, technical look and feel

```html
<!DOCTYPE html>
<html lang="en">
<head>
<meta charset="utf-8">
<title>KM Works – Business Card</title>
<link rel="stylesheet" href="https://fonts.googleapis.com/css2?family=Montserrat:wght@600;700&family=Roboto:wght@400;500;700&display=swap">
<style>
  :root {
    --bg: #e9e7e4;
    --card: #f4f4f3;
    --blue: #0d4a8f;
    --red: #b3202a;
    --grey: #8f9296;
    --text: #55585c;
  }
  * { box-sizing: border-box; margin: 0; padding: 0; }
  html, body { width: 1200px; height: 961px; overflow: hidden; }
  body {
    background: var(--bg);
    font-family: "Roboto", Arial, sans-serif;
    position: relative;
  }
  .card {
    position: absolute;
    width: 620px;
    height: 354px;
    background: var(--card);
    box-shadow: 0 6px 18px rgba(0,0,0,0.12);
  }
  .card--front { left: 90px; top: 80px; }
  .card--back { left: 490px; top: 520px; }

  .brand {
    display: flex;
    align-items: center;
    gap: 12px;
    color: var(--blue);
    font-family: "Roboto", Arial, sans-serif;
    font-weight: 700;
    letter-spacing: 1px;
  }
  .brand__mark { background: var(--red); flex: none; }

  .card--front .brand {
    position: absolute;
    left: 0; right: 0; top: 118px;
    justify-content: center;
    font-size: 62px;
  }
  .card--front .brand__mark { width: 18px; height: 18px; }
  .front__web {
    position: absolute;
    left: 0; right: 0; top: 222px;
    text-align: center;
    color: var(--blue);
    font-size: 17px;
    letter-spacing: 0.5px;
  }

  .card--back .brand {
    position: absolute;
    right: 42px; top: 48px;
    font-size: 40px;
    gap: 10px;
  }
  .card--back .brand__mark { width: 12px; height: 12px; }

  .address {
    position: absolute;
    right: 42px; top: 128px;
    text-align: right;
    font-size: 15px;
    line-height: 21px;
    color: var(--text);
  }
  .address__company { color: var(--blue); font-weight: 500; }

  .accent-bar {
    position: absolute;
    left: 0; top: 212px;
    width: 14px; height: 50px;
    background: var(--blue);
  }
  .person {
    position: absolute;
    left: 44px; top: 190px;
  }
  .person__name {
    font-family: "Montserrat", Arial, sans-serif;
    font-weight: 700;
    font-size: 21px;
    color: var(--blue);
    letter-spacing: 0.3px;
  }
  .person__role {
    font-size: 17px;
    color: var(--red);
    margin-top: 2px;
  }
  .contacts {
    list-style: none;
    margin-top: 12px;
    margin-left: 16px;
    font-size: 15px;
    color: var(--text);
    line-height: 23px;
  }
  .contacts li { display: flex; align-items: center; gap: 8px; }
  .contacts svg { width: 14px; height: 14px; flex: none; fill: var(--red); }
</style>
</head>
<body>

<section class="card card--front" aria-label="Card front">
  <div class="brand"><span class="brand__mark"></span>KM Works</div>
  <p class="front__web">www.kmworks.example</p>
</section>

<section class="card card--back" aria-label="Card back">
  <div class="brand"><span class="brand__mark"></span>KM Works</div>

  <address class="address" style="font-style:normal">
    <div class="address__company">KM Works, Inc.</div>
    <div>48 Harlow Lane, Suite 200</div>
    <div>Brookfield, GA 30999</div>
  </address>

  <div class="accent-bar"></div>

  <div class="person">
    <div class="person__name">MARCO FERRANDI</div>
    <div class="person__role">Director</div>
    <ul class="contacts">
      <li>
        <svg viewBox="0 0 24 24" aria-hidden="true"><path d="M6.6 10.8a15.1 15.1 0 0 0 6.6 6.6l2.2-2.2a1 1 0 0 1 1-.25 11.4 11.4 0 0 0 3.6.57 1 1 0 0 1 1 1V20a1 1 0 0 1-1 1A17 17 0 0 1 3 4a1 1 0 0 1 1-1h3.5a1 1 0 0 1 1 1c0 1.25.2 2.45.57 3.57a1 1 0 0 1-.25 1z"/></svg>
        (555) 014.2761
      </li>
      <li>
        <svg viewBox="0 0 24 24" aria-hidden="true"><path d="M2 5h20v14H2z M4 7l8 6 8-6" fill="var(--red)"/><path d="M4 7l8 6 8-6" fill="none" stroke="#fff" stroke-width="1.6"/></svg>
        mferrandi@kmworks.example
      </li>
      <li>
        <svg viewBox="0 0 24 24" aria-hidden="true"><circle cx="12" cy="12" r="9" fill="none" stroke="var(--red)" stroke-width="2"/><path d="M3 12h18M12 3c3 3 3 15 0 18M12 3c-3 3-3 15 0 18" fill="none" stroke="var(--red)" stroke-width="1.6"/></svg>
        www.kmworks.example
      </li>
    </ul>
  </div>
</section>

</body>
</html>
```